Events Calendar and Event Reminder Postcard Design

We need a Calendar of Events and an Event Reminder Postcard that utilize the same design look to create a uniform branding appearance. The design format for the 11" x 17" calendar page should be somewhat similar to the attached calendar sample, but not exactly the same. The 4.25" x 5.5" (4 up on an 8.5"x11" sheet) postcard needs to be able to accommodate the amount of information referenced in the attached example of our existing event reminder postcard. Our logo has been uploaded and should be included on both pieces as well. Prefer Adobe Illustrator files.

Target Market(s)

PJR Membership

Industry/Entity Type

Events

Font styles to use
Serif
Sans Serif

Requirements
Must have
• See Description and the attached sample files. Prefer Adobe InDesign files
Should not have
• Should not be cartoonish in nature

```html
<!DOCTYPE html>
<html lang="en">
<head>
<meta charset="utf-8">
<title>PJR 2017 Calendar of Events and Event Reminder Postcard</title>
<link rel="stylesheet" href="https://fonts.googleapis.com/css2?family=Josefin+Sans:wght@300;400&family=Open+Sans:wght@400;700&family=Roboto+Condensed:wght@700&display=swap">
<style>
:root{
  --taupe:#6a655d;
  --teal:#7f9a9a;
  --ink:#47423d;
  --rule:#b9b6b1;
  --paper:#ffffff;
  --canvas:#ffffff;
}
*{box-sizing:border-box;margin:0;padding:0}
html,body{width:1200px;height:1000px;overflow:hidden;background:var(--canvas)}
body{position:relative;font-family:"Open Sans",sans-serif;color:var(--ink)}

/* Calendar page */
.calendar{position:absolute;left:57px;top:17px;width:633px;height:978px;background:var(--paper);box-shadow:0 0 3px rgba(0,0,0,.12)}
.calendar-banner{position:absolute;left:0;top:13px;width:390px;height:66px}
.calendar-banner svg{position:absolute;inset:0}
.banner-year{position:absolute;left:25px;top:8px;font-family:"Josefin Sans",sans-serif;font-weight:300;font-size:50px;line-height:56px;color:var(--teal)}
.banner-title{position:absolute;left:151px;top:7px;font-family:"Josefin Sans",sans-serif;font-weight:300;font-size:27px;line-height:28px;color:#fff;letter-spacing:.5px}
.brand-mark{position:absolute;left:433px;top:70px;display:flex;align-items:center;gap:12px;font-family:"Josefin Sans",sans-serif;font-weight:400;font-size:62px;line-height:1;color:var(--taupe)}
.brand-square{width:22px;height:22px;background:var(--teal)}
.calendar-intro{position:absolute;left:23px;top:91px;width:370px;font-size:12.6px;line-height:15.3px}

.months{position:absolute;top:228px;left:7px;display:flex}
.month-column{width:210px}
.month-column:nth-child(2){width:210px}
.month{margin-bottom:12px}
.month-name{font-family:"Josefin Sans",sans-serif;font-weight:300;font-size:19px;line-height:22px;height:27px;color:var(--taupe);text-transform:uppercase}
.event{display:flex;height:53px}
.event-date{width:52px;font-family:"Josefin Sans",sans-serif;font-weight:300;font-size:35px;line-height:36px;color:var(--teal);padding-left:2px}
.event-text{border-left:1px solid var(--rule);height:44px;padding-left:5px;width:142px;font-size:7.6px;line-height:9.6px;color:var(--ink)}
.event-text b{font-weight:700}

.calendar-footer{position:absolute;left:5px;bottom:13px;font-size:8.4px;color:var(--teal)}
.calendar-base{position:absolute;left:0;right:0;bottom:3px;height:4px;background:var(--taupe)}

/* Postcard */
.postcard{position:absolute;left:783px;top:235px;width:294px;height:227px;background:var(--paper);border:1px solid #e1dfdc}
.postcard-band{position:absolute;left:0;top:0;width:202px;height:90px}
.postcard-headline{position:absolute;left:14px;top:10px;font-family:"Roboto Condensed",sans-serif;font-weight:700;font-size:14.2px;line-height:17.5px;color:#fff}
.postcard-brand{position:absolute;left:213px;top:28px;display:flex;align-items:center;gap:5px;font-family:"Josefin Sans",sans-serif;font-size:26px;line-height:1;color:var(--taupe)}
.postcard-brand .brand-square{width:9px;height:9px}
.host-name{position:absolute;left:16px;top:120px;font-family:"Open Sans",sans-serif;font-weight:700;font-size:21px;letter-spacing:-.5px;color:var(--taupe)}
.postcard-body{position:absolute;left:116px;top:103px;width:168px;font-size:5.3px;line-height:7px}
.postcard-call{position:absolute;left:116px;top:172px;font-family:"Roboto Condensed",sans-serif;font-weight:700;font-size:12.5px;color:var(--teal)}
.postcard-or{position:absolute;left:170px;top:192px;font-size:7px}
.postcard-web{position:absolute;left:116px;top:205px;font-family:"Roboto Condensed",sans-serif;font-weight:700;font-size:9.4px;color:var(--teal)}
.postcard-base{position:absolute;left:0;right:0;bottom:2px;height:3px;background:var(--taupe)}
</style>
</head>
<body>

<section class="calendar">
  <header class="calendar-banner">
    <svg width="390" height="66" viewBox="0 0 390 66"><polygon points="0,0 298,0 390,66 0,66" fill="var(--taupe)"/></svg>
    <span class="banner-year">2017</span>
    <h1 class="banner-title">CALENDAR<br>OF EVENTS</h1>
  </header>
  <div class="brand-mark"><span class="brand-square"></span>PJR</div>
  <p class="calendar-intro">Lorem ipsum dolor sit amet, consectetur adipiscing elit, sed do eiusmod tempor incididunt ut labore et<br>Lorem ipsum dolor sit amet, consectetur adipiscing elit, sed do eiusmod tempor incididunt ut labore et<br>Lorem ipsum dolor sit amet, consectetur adipiscing elit, sed do eiusmod tempor incididunt ut labore et</p>

  <div class="months">
    <div class="month-column">
      <div class="month"><h2 class="month-name">January</h2>
        <div class="event"><span class="event-date">02</span><p class="event-text"><b>Lorem ipsum</b> dolor sit amet, consectetur adipiscing elit, sed do eiusmod tempor incididunt ut labore et</p></div>
        <div class="event"><span class="event-date">12</span><p class="event-text"><b>Lorem ipsum</b> dolor sit amet, consectetur adipiscing elit, sed do eiusmod tempor incididunt ut labore et tetur adipiscing elit, sed do eiusmod</p></div>
        <div class="event"><span class="event-date">30</span><p class="event-text"><b>Lorem ipsum</b> dolor sit amet, consectetur adipiscing elit, sed do eiusmod tempor incididunt ut labore et tetur adipiscing elit, sed do eiusmod</p></div>
      </div>
      <div class="month"><h2 class="month-name">February</h2>
        <div class="event"><span class="event-date">10</span><p class="event-text"><b>Lorem ipsum</b> dolor sit amet, consectetur adipiscing elit, sed do eiusmod tempor incididunt ut labore et</p></div>
        <div class="event"><span class="event-date">25</span><p class="event-text"><b>Lorem ipsum</b> dolor sit amet, consectetur adipiscing elit, sed do eiusmod tempor incididunt ut labore et tetur adipiscing elit, sed do eiusmod</p></div>
      </div>
      <div class="month"><h2 class="month-name">March</h2>
        <div class="event"><span class="event-date">08</span><p class="event-text"><b>Lorem ipsum</b> dolor sit amet, consectetur adipiscing elit, sed do eiusmod tempor incididunt ut labore et</p></div>
        <div class="event"><span class="event-date">19</span><p class="event-text"><b>Lorem ipsum</b> dolor sit amet, consectetur adipiscing elit, sed do eiusmod tempor incididunt ut labore et tetur adipiscing elit, sed do eiusmod</p></div>
        <div class="event"><span class="event-date">23</span><p class="event-text"><b>Lorem ipsum</b> dolor sit amet, consectetur adipiscing elit, sed do eiusmod tempor incididunt ut labore et tetur adipiscing elit, sed do eiusmod</p></div>
      </div>
      <div class="month"><h2 class="month-name">April</h2>
        <div class="event"><span class="event-date">03</span><p class="event-text"><b>Lorem ipsum</b> dolor sit amet, consectetur adipiscing elit, sed do eiusmod tempor incididunt ut labore et</p></div>
        <div class="event"><span class="event-date">13</span><p class="event-text"><b>Lorem ipsum</b> dolor sit amet, consectetur adipiscing elit, sed do eiusmod tempor incididunt ut labore et tetur adipiscing elit, sed do eiusmod</p></div>
      </div>
    </div>

    <div class="month-column">
      <div class="month"><h2 class="month-name">May</h2>
        <div class="event"><span class="event-date">01</span><p class="event-text"><b>Lorem ipsum</b> dolor sit amet, consectetur adipiscing elit, sed do eiusmod tempor incididunt ut labore et</p></div>
        <div class="event"><span class="event-date">23</span><p class="event-text"><b>Lorem ipsum</b> dolor sit amet, consectetur adipiscing elit, sed do eiusmod tempor incididunt ut labore et tetur adipiscing elit, sed do eiusmod</p></div>
      </div>
      <div class="month"><h2 class="month-name">June</h2>
        <div class="event"><span class="event-date">10</span><p class="event-text"><b>Lorem ipsum</b> dolor sit amet, consectetur adipiscing elit, sed do eiusmod tempor incididunt ut labore et</p></div>
        <div class="event"><span class="event-date">25</span><p class="event-text"><b>Lorem ipsum</b> dolor sit amet, consectetur adipiscing elit, sed do eiusmod tempor incididunt ut labore et tetur adipiscing elit, sed do eiusmod</p></div>
      </div>
      <div class="month"><h2 class="month-name">July</h2>
        <div class="event"><span class="event-date">05</span><p class="event-text"><b>Lorem ipsum</b> dolor sit amet, consectetur adipiscing elit, sed do eiusmod tempor incididunt ut labore et</p></div>
        <div class="event"><span class="event-date">17</span><p class="event-text"><b>Lorem ipsum</b> dolor sit amet, consectetur adipiscing elit, sed do eiusmod tempor incididunt ut labore et tetur adipiscing elit, sed do eiusmod</p></div>
        <div class="event"><span class="event-date">22</span><p class="event-text"><b>Lorem ipsum</b> dolor sit amet, consectetur adipiscing elit, sed do eiusmod tempor incididunt ut labore et tetur adipiscing elit, sed do eiusmod</p></div>
      </div>
      <div class="month"><h2 class="month-name">August</h2>
        <div class="event"><span class="event-date">09</span><p class="event-text"><b>Lorem ipsum</b> dolor sit amet, consectetur adipiscing elit, sed do eiusmod tempor incididunt ut labore et</p></div>
        <div class="event"><span class="event-date">23</span><p class="event-text"><b>Lorem ipsum</b> dolor sit amet, consectetur adipiscing elit, sed do eiusmod tempor incididunt ut labore et tetur adipiscing elit, sed do eiusmod</p></div>
        <div class="event"><span class="event-date">31</span><p class="event-text"><b>Lorem ipsum</b> dolor sit amet, consectetur adipiscing elit, sed do eiusmod tempor incididunt ut labore et tetur adipiscing elit, sed do eiusmod</p></div>
      </div>
    </div>

    <div class="month-column">
      <div class="month"><h2 class="month-name">Sepetember</h2>
        <div class="event"><span class="event-date">01</span><p class="event-text"><b>Lorem ipsum</b> dolor sit amet, consectetur adipiscing elit, sed do eiusmod tempor incididunt ut labore et</p></div>
        <div class="event"><span class="event-date">12</span><p class="event-text"><b>Lorem ipsum</b> dolor sit amet, consectetur adipiscing elit, sed do eiusmod tempor incididunt ut labore et tetur adipiscing elit, sed do eiusmod</p></div>
        <div class="event"><span class="event-date">20</span><p class="event-text"><b>Lorem ipsum</b> dolor sit amet, consectetur adipiscing elit, sed do eiusmod tempor incididunt ut labore et tetur adipiscing elit, sed do eiusmod</p></div>
      </div>
      <div class="month"><h2 class="month-name">October</h2>
        <div class="event"><span class="event-date">17</span><p class="event-text"><b>Lorem ipsum</b> dolor sit amet, consectetur adipiscing elit, sed do eiusmod tempor incididunt ut labore et</p></div>
        <div class="event"><span class="event-date">26</span><p class="event-text"><b>Lorem ipsum</b> dolor sit amet, consectetur adipiscing elit, sed do eiusmod tempor incididunt ut labore et tetur adipiscing elit, sed do eiusmod</p></div>
      </div>
      <div class="month"><h2 class="month-name">November</h2>
        <div class="event"><span class="event-date">12</span><p class="event-text"><b>Lorem ipsum</b> dolor sit amet, consectetur adipiscing elit, sed do eiusmod tempor incididunt ut labore et</p></div>
        <div class="event"><span class="event-date">19</span><p class="event-text"><b>Lorem ipsum</b> dolor sit amet, consectetur adipiscing elit, sed do eiusmod tempor incididunt ut labore et tetur adipiscing elit, sed do eiusmod</p></div>
        <div class="event"><span class="event-date">24</span><p class="event-text"><b>Lorem ipsum</b> dolor sit amet, consectetur adipiscing elit, sed do eiusmod tempor incididunt ut labore et tetur adipiscing elit, sed do eiusmod</p></div>
      </div>
      <div class="month"><h2 class="month-name">December</h2>
        <div class="event"><span class="event-date">07</span><p class="event-text"><b>Lorem ipsum</b> dolor sit amet, consectetur adipiscing elit, sed do eiusmod tempor incididunt ut labore et</p></div>
        <div class="event"><span class="event-date">29</span><p class="event-text"><b>Lorem ipsum</b> dolor sit amet, consectetur adipiscing elit, sed do eiusmod tempor incididunt ut labore et tetur adipiscing elit, sed do eiusmod</p></div>
      </div>
    </div>
  </div>

  <p class="calendar-footer">1480 Alder Ave SE Suite #200, Salem OR 97301 Phone: (555) 214-1500 | Fax: (555) 214-0651 | www.pjrbuilders.org</p>
  <div class="calendar-base"></div>
</section>

<section class="postcard">
  <svg class="postcard-band" width="202" height="90" viewBox="0 0 202 90"><polygon points="0,0 152,0 202,90 0,90" fill="var(--taupe)"/></svg>
  <h2 class="postcard-headline">Register Today<br>for the Feb. 7th<br>PJR Off-the-Clock<br>at Harlow's Home Center</h2>
  <div class="postcard-brand"><span class="brand-square"></span>PJR</div>
  <div class="host-name">Harlow's</div>
  <p class="postcard-body">Join us for an exciting Off-the-Clock hosted by Harlow's Home Center on Tuesday, February 7th. Take time after your busy day to relax and meet the appliance experts to discuss your upcoming Tour home or see what's new in the appliance industry. This is not your typical Off-the-Clock as there will be lots of chances to win valuable raffle prizes all while mixing and mingling with your fellow Association members.</p>
  <p class="postcard-call">CALL the PJR (555) 214-1500</p>
  <p class="postcard-or">or register online</p>
  <p class="postcard-web">www.pjrbuilders.org</p>
  <div class="postcard-base"></div>
</section>

</body>
</html>
```